Wedding Decor and Entertianment business card

Company - We run a weddings and events company called Amber Finch, we provide most entertainment and decor services to our customers.

Initial idea is ....
A simple business card with logo on the front, this will be spot varnish. On a matt black background.
The reverse will be simple contact information.

But happy to try things outside of the box and would welcome some crazy ideas.

Target Market(s)

wedding couples - 21 - 40
High end wedding venues.

Industry/Entity Type

Wedding

Contact Information for Business Card

01492 718 263
amberfinchevents.co.uk
rowan@amberfinchevents.co.uk
or
helena@amberfinchevents.co.uk

Requirements
Nice to have
• black matt background with spot varnish logo on the front.

```html
<!DOCTYPE html>
<html lang="en">
<head>
<meta charset="utf-8">
<title>Amber Finch — Business Card</title>
<link href="https://fonts.googleapis.com/css2?family=Jost:wght@300;400&family=Open+Sans:wght@400;700&display=swap" rel="stylesheet">
<style>
  :root {
    --backdrop: #e8e5e1;
    --card-black: #232323;
    --card-black-light: #333333;
    --card-white: #ffffff;
    --plum: #7e4f7e;
    --ink: #1f2226;
    --ink-soft: #3a3d42;
    --paper-white: #f4f4f4;
  }
  * { box-sizing: border-box; margin: 0; padding: 0; }
  html, body {
    width: 1200px; height: 900px; overflow: hidden;
    background: var(--backdrop);
  }
  .canvas { position: relative; width: 1200px; height: 900px; }

  .card {
    position: absolute;
    width: 600px; height: 343px;
    box-shadow: 0 10px 28px rgba(0,0,0,0.18);
  }

  /* Front: matt black with brand name */
  .card-front {
    left: 530px; top: 70px;
    background: linear-gradient(135deg, var(--card-black) 0%, var(--card-black-light) 55%, var(--card-black) 100%);
  }
  .card-front .brand-name {
    position: absolute; left: 0; right: 0; top: 150px;
    text-align: center;
    font-family: "Jost", sans-serif; font-weight: 300;
    font-size: 34px; letter-spacing: 0.42em;
    color: var(--paper-white);
    padding-left: 0.42em;
  }

  /* Back: contact side */
  .card-back {
    left: 70px; top: 470px;
    background: var(--card-white);
  }
  .card-back .shapes { position: absolute; inset: 0; }
  .person { position: absolute; left: 78px; top: 30px; font-family: "Open Sans", sans-serif; }
  .person-name { font-weight: 700; font-size: 17px; color: var(--plum); line-height: 1.1; }
  .person-role { font-size: 13px; color: var(--ink); margin-top: 2px; }

  .contact-list {
    position: absolute; left: 26px; top: 168px;
    list-style: none;
    font-family: "Open Sans", sans-serif; font-size: 13.5px; color: var(--ink);
  }
  .contact-list li { display: flex; align-items: center; gap: 9px; height: 21px; }
  .contact-list svg { width: 11px; height: 11px; fill: var(--plum); flex: none; }

  .brand-lockup {
    position: absolute; left: 262px; top: 150px;
    font-family: "Jost", sans-serif; font-weight: 300;
    font-size: 31px; letter-spacing: 0.4em; line-height: 1;
    color: var(--ink);
  }
  .brand-lockup .word-second { display: block; margin-left: 96px; margin-top: 12px; }
</style>
</head>
<body>
<main class="canvas">

  <section class="card card-front" aria-label="Card front">
    <p class="brand-name">AMBER FINCH</p>
  </section>

  <section class="card card-back" aria-label="Card back">
    <svg class="shapes" viewBox="0 0 600 343" width="600" height="343" aria-hidden="true">
      <polygon points="0,30 54,30 40,62 0,62" fill="var(--plum)"/>
      <polygon points="60,30 72,30 72,62 46,62" fill="var(--ink)"/>
      <polygon points="0,252 332,252 314,284 0,284" fill="var(--plum)"/>
      <polygon points="338,284 600,284 600,330 312,330" fill="var(--ink)"/>
    </svg>

    <div class="person">
      <p class="person-name">Rowan Ellery</p>
      <p class="person-role">Managing Director</p>
    </div>

    <ul class="contact-list">
      <li>
        <svg viewBox="0 0 24 24"><path d="M6.6 10.8a15.1 15.1 0 0 0 6.6 6.6l2.2-2.2a1 1 0 0 1 1-.25 11.4 11.4 0 0 0 3.6.57 1 1 0 0 1 1 1V20a1 1 0 0 1-1 1A17 17 0 0 1 3 4a1 1 0 0 1 1-1h3.5a1 1 0 0 1 1 1c0 1.25.2 2.45.57 3.57a1 1 0 0 1-.25 1z"/></svg>
        01492 718 263
      </li>
      <li>
        <svg viewBox="0 0 24 24"><path d="M2 5h20v14H2z M2 5l10 8 10-8" fill="var(--plum)"/></svg>
        rowan@amberfinchevents.co.uk
      </li>
      <li>
        <svg viewBox="0 0 24 24"><circle cx="12" cy="12" r="10"/></svg>
        amberfinchevents.co.uk
      </li>
    </ul>

    <p class="brand-lockup">AMBER<span class="word-second">FINCH</span></p>
  </section>

</main>
</body>
</html>
```